Etiketten für Limonade und Eistee
Zielgruppe
Foodtruck & Catering - Philosophie FRISCH / REGIONAL / AUTHENTISCH
Zielgruppe 20-45 Jahre mit einem Bewusstsein für frische & gesunde Ernährung, Flair für Genusszeit & Zeit mit Freunden.
Weitere Informationen: www.aukiebitz.ch
Aufgabenstellung
Flaschen-Etikett für Kiebitz Limonade und Kiebitz Eistee (Vorlage siehe 'Wolfeler Eistee)
Offizielle Produktbezeichnung, Zutaten und Nährwertangaben (alle Angaben in der Vorlage auf linker Seite) bitte mit Platzhalter versehen. Die definitiven Angaben kommen noch.
Ein Produkt von: Au Kiebitz Gmbh, Lindenhalde 14, CH-4633 Lindwil
www.aukiebitz.ch / Verweis auf Instagram, Facebook, TikTok (@aukiebitz)
Gut lesbar
Abgefüllt von: wie auf Vorlage, möglichst klein
Hinweis: Kühl und dunkel lagern, Einwegflasche - möglichst klein / 33cl - gut lesbar irgendwo
Limonade: Titel Kiebitz Limonade oder Kiebitz Limo (Holunderblüte, Marokkanische Minze, Zitronensaft) - sommerlich frisch. Farbe des Getränk ca. #F5fbf2 (Peppermint).
Eistee: Titel Kiebitz Eistee (Kirsche, Zitronensaft, Agaven(dick)saft) - aus frischem Tee gebrüht, herb & erfrischend. Farbe des Getränk ca. #D66464 (Chestnut Rose)
Wünsche & Vorgaben:
Schlichtes Design, Schrift gut lesbar auf neutralem Hintergrund (z.B. weiss oder Pergament). Einfache Formen als Gestaltungsmerkmale, in passenden Farben zum Getränk. Soll auffallen (für Verkauf im Regal), aber trotzdem elegant und dezent wirken (für Catering).
Unser Logo soll ersichtlich sein, muss aber nicht im Zentrum stehen. Der Kiebitz kann als eigenständiger Teil des Logo ersichtlich sein, muss aber auch nicht im Zentrum stehen.
Es sind einige Bilder von anderen Getränke im Anhang. Diese dienen als Hilfe, in welche Richtung es gehen kann/soll. Ihr müsst euch aber nicht zwingend daran halten. Die Variante 'Tobru' mit den Streifen sagt uns am ehesten zu.

```html
<!DOCTYPE html>
<html lang="de">
<head>
<meta charset="utf-8">
<title>Kiebitz Limo &amp; Kiebitz Eistee – Etiketten</title>
<link rel="stylesheet" href="https://fonts.googleapis.com/css2?family=Barlow+Condensed:wght@400;500;600&family=Jost:wght@400;500;600;700&display=swap">
<style>
  :root{
    --paper:#f5f5f5;
    --ink:#1d1d1d;
    --limo:#acd49e;
    --eistee:#eca0a0;
    --stage:#e2e2e2;
    --art:#d9d9d9;
    --info:"Barlow Condensed", sans-serif;
    --display:"Jost", sans-serif;
  }
  *{margin:0;padding:0;box-sizing:border-box}
  html,body{width:1200px;height:2554px;overflow:hidden;background:var(--paper);color:var(--ink)}
  .canvas{position:relative;width:1200px;height:2554px}
  .label{position:absolute;left:0;width:1200px;height:758px;background:var(--paper);overflow:hidden}
  .label--limo{top:0;--accent:var(--limo)}
  .label--eistee{top:758px;--accent:var(--eistee);border-top:1px solid #e8e8e8}
  .band{position:absolute;left:0;width:1200px;height:66px;background:var(--accent)}
  .t{position:absolute;font-family:var(--info);font-size:19px;line-height:24px;white-space:nowrap}
  .b{font-weight:600}
  .m{font-weight:500}
  .small{font-size:16px;line-height:18px;font-weight:600}
  .tiny{font-size:13px;line-height:15px}
  .val{position:absolute;font-family:var(--info);font-size:19px;line-height:24px}
  .volume{position:absolute;left:32px;top:672px;font-family:var(--display);font-size:23px;white-space:nowrap}
  .volume .e{font-size:32px;font-weight:400;margin-right:8px}
  .center{position:absolute;left:0;width:1238px;text-align:center;font-family:var(--display)}
  .brand-name{top:128px;font-size:42px;font-weight:400;letter-spacing:1px}
  .product{top:168px;font-size:84px;font-weight:600;line-height:84px;letter-spacing:1px}
  .claim{top:594px;font-size:17px;font-weight:600;letter-spacing:3px}
  .flavours{top:655px;font-size:14px;line-height:21.5px;font-weight:500;letter-spacing:2.6px}
  .mark{position:absolute;left:588px;top:90px;width:66px;height:18px;border-radius:9px;background:var(--ink)}
  .portrait{position:absolute;left:506px;top:300px;width:227px;height:227px;border-radius:50%;border:3px solid var(--ink);background:var(--art)}
  .maker{position:absolute;left:1034px;top:112px;width:86px;height:86px;border-radius:50%;border:2px dashed var(--ink);display:flex;align-items:center;justify-content:center;text-align:center;font-family:var(--info);font-size:14px;line-height:14px;font-weight:500}
  .social{position:absolute;left:1021px;top:370px;display:flex;align-items:center;gap:6px;font-family:var(--info);font-size:14px;font-weight:500}
  .social .dot{width:14px;height:14px;border:2px solid var(--ink);border-radius:50%}
  .stage{position:absolute;left:0;top:1517px;width:1200px;height:1037px;background:radial-gradient(ellipse at 50% 45%,#f0f0f0 0%,var(--stage) 70%,#d6d6d6 100%)}
  .bottle{position:absolute;top:90px;width:222px;height:895px;border-radius:70px 70px 36px 36px}
  .bottle--eistee{left:254px;background:linear-gradient(90deg,#b24a4a,#d66464 40%,#c45858)}
  .bottle--limo{left:728px;background:linear-gradient(90deg,#8aa596,#c3d8cc 40%,#9fb8aa)}
</style>
</head>
<body>
<main class="canvas">

  <!-- Limonade -->
  <section class="label label--limo">
    <div class="band" style="top:332px"></div>
    <div class="band" style="top:453px"></div>
    <div class="band" style="top:571px"></div>

    <p class="t m" style="left:35px;top:152px">Limonade mit<br>Holunderblüte, Marokkanischer Minze<br>und Zitronensaft</p>
    <p class="t" style="left:34px;top:246px"><span class="b">Zutaten:</span> Wasser, Holunderblütensirup<br>Zucker, Minzextrakt, Zitronendirektsaft<br>(mind. X%)</p>
    <p class="t m" style="left:33px;top:344px">Kühl und dunkel lagern</p>
    <p class="t m" style="left:33px;top:403px">Nährwertangabe pro 100ml</p>
    <p class="t" style="left:33px;top:427px">Energie</p><p class="val" style="left:137px;top:427px">25,6 kcal / 107,4 KJ</p>
    <p class="t" style="left:33px;top:464px">Fett<br>davon ges. Fettsäuren</p><p class="val" style="left:228px;top:468px">0,0 g<br>0,0 g</p>
    <p class="t" style="left:33px;top:524px">Kohlenhydrate<br>davon Zucker</p><p class="val" style="left:228px;top:521px">6,2 g<br>6,2 g</p>
    <p class="t" style="left:33px;top:583px">Eiweiss<br>Salz</p><p class="val" style="left:232px;top:585px">0,1 g<br>0,0 g</p>
    <p class="volume"><span class="e">e33cl</span> Einwegflasche</p>

    <div class="mark" role="img" aria-label="Kleines Schnurrbart-Ornament"></div>
    <p class="center brand-name">Kiebitz</p>
    <p class="center product">LIMO</p>
    <div class="portrait" role="img" aria-label="Illustration der Markenfigur mit Flasche"></div>
    <p class="center claim">SOMMERLICH FRISCH</p>
    <p class="center flavours">HOLUNDERBLÜTE<br>MAROKKANISCHE MINZE<br>ZITRONENSAFT</p>

    <div class="maker">Au<br>Kiebitz</div>
    <p class="t" style="left:1021px;top:208px"><span class="m">Ein Produkt von:</span><br>Au Kiebitz Gmbh<br>Lindenhalde 14<br>CH-4633 Lindwil<br>www.aukiebitz.ch</p>
    <p class="t m" style="left:1021px;top:340px">Folge uns auf</p>
    <div class="social"><span class="dot"></span>@aukiebitz</div>
    <p class="t small" style="left:1018px;top:462px">Abgefüllt von:<br>Frischwerk<br>Getränke AG</p>
    <p class="t tiny" style="left:1018px;top:524px">Alte Mühle Hofgut<br>Mühleweg 9<br>CH-3086, Zimmerwald</p>
    <p class="t m" style="left:1017px;top:645px">Mindestens haltbar bis:</p>
  </section>

  <!-- Eistee -->
  <section class="label label--eistee">
    <div class="band" style="top:332px"></div>
    <div class="band" style="top:453px"></div>
    <div class="band" style="top:571px"></div>

    <p class="t m" style="left:35px;top:126px">Eistee mit<br>Kirsche, Zitronensaft<br>und Agavendicksaft</p>
    <p class="t" style="left:34px;top:222px"><span class="b">Zutaten:</span> Wasser, Tee, Kirschsaft<br>Zucker, Zitronendirektsaft<br>(mind. X%), Agavendicksaft</p>
    <p class="t m" style="left:33px;top:344px">Kühl und dunkel lagern</p>
    <p class="t m" style="left:35px;top:403px">Nährwertangabe pro 100ml</p>
    <p class="t" style="left:35px;top:427px">Energie</p><p class="val" style="left:139px;top:427px">25,6 kcal / 107,4 KJ</p>
    <p class="t" style="left:35px;top:464px">Fett<br>davon ges. Fettsäuren</p><p class="val" style="left:230px;top:468px">0,0 g<br>0,0 g</p>
    <p class="t" style="left:35px;top:524px">Kohlenhydrate<br>davon Zucker</p><p class="val" style="left:230px;top:521px">6,2 g<br>6,2 g</p>
    <p class="t" style="left:35px;top:583px">Eiweiss<br>Salz</p><p class="val" style="left:234px;top:585px">0,1 g<br>0,0 g</p>
    <p class="volume" style="top:673px"><span class="e">e33cl</span> Einwegflasche</p>

    <div class="mark" role="img" aria-label="Kleines Schnurrbart-Ornament"></div>
    <p class="center brand-name">Kiebitz</p>
    <p class="center product">EISTEE</p>
    <div class="portrait" role="img" aria-label="Illustration der Markenfigur mit Flasche"></div>
    <p class="center claim">HERB &amp; ERFRISCHEND</p>
    <p class="center flavours">KIRSCHE<br>ZITRONENSAFT<br>AGAVENDICKSAFT</p>

    <div class="maker">Au<br>Kiebitz</div>
    <p class="t" style="left:1021px;top:208px"><span class="m">Ein Produkt von:</span><br>Au Kiebitz Gmbh<br>Lindenhalde 14<br>CH-4633 Lindwil<br>www.aukiebitz.ch</p>
    <p class="t m" style="left:1021px;top:340px">Folge uns auf</p>
    <div class="social"><span class="dot"></span>@aukiebitz</div>
    <p class="t small" style="left:1018px;top:462px">Abgefüllt von:<br>Frischwerk<br>Getränke AG</p>
    <p class="t tiny" style="left:1018px;top:524px">Alte Mühle Hofgut<br>Mühleweg 9<br>CH-3086, Zimmerwald</p>
    <p class="t m" style="left:1017px;top:645px">Mindestens haltbar bis:</p>
  </section>

  <!-- Flaschen -->
  <section class="stage">
    <div class="bottle bottle--eistee" role="img" aria-label="Flasche Kiebitz Eistee mit Etikett"></div>
    <div class="bottle bottle--limo" role="img" aria-label="Flasche Kiebitz Limo mit Etikett"></div>
  </section>

</main>
</body>
</html>
```